Card for Maori themed strategy game

Visual design of a type of card from a board game.
The card has a front and a back, back being a single large image, and with one of three small icons (in white) to represent which of the three periods of the game it is from, but otherwise there is no difference in the backs.
The front side carries most of the information, and hopefully an attractive design. Functionally, from top to bottom it has a title, a large text field, a type line, another text field, and some tracking information at the very bottom. Current layout with placeholder art is attached.
Note that the relative size of the two text boxes will vary from card to card.
The colour pallete is intended to be red black and white, for this particular design focusing primarily on red.

```html
<!DOCTYPE html>
<html lang="en">
<head>
<meta charset="utf-8">
<title>Influenza Epidemic – Card Front</title>
<link rel="stylesheet" href="https://fonts.googleapis.com/css2?family=Ubuntu:wght@700&family=Quicksand:wght@600&display=swap">
<style>
  :root {
    --page: #fefefe;
    --red-deep: #6e0a0e;
    --red-mid: #8e1117;
    --red-bright: #b3202a;
    --scroll-edge: #d6cbb0;
    --scroll-shade: #c4b797;
    --parchment: #f5f1e8;
    --ink: #111111;
    --title-light: #f2e8dc;
    --title-warm: #c9b6a4;
  }
  html, body {
    margin: 0;
    width: 1200px;
    height: 1200px;
    overflow: hidden;
    background: var(--page);
  }
  .card {
    position: absolute;
    left: 418px;
    top: 318px;
    width: 357px;
    height: 499px;
    border-radius: 20px;
    background: var(--red-mid);
    box-shadow: 8px 8px 8px rgba(0,0,0,0.35);
    overflow: hidden;
  }
  .card-pattern {
    position: absolute;
    inset: 0;
    background:
      radial-gradient(ellipse at 75% 8%, var(--red-bright) 0%, transparent 45%),
      radial-gradient(ellipse at 50% 55%, var(--red-bright) 0%, transparent 50%),
      linear-gradient(180deg, var(--red-deep), var(--red-mid) 50%, var(--red-deep));
  }
  .card-title, .type-line {
    position: absolute;
    left: 0;
    width: 100%;
    margin: 0;
    text-align: center;
    font-family: "Ubuntu", sans-serif;
    font-weight: 700;
    text-shadow: 1px 2px 2px rgba(0,0,0,0.5);
  }
  .card-title {
    top: 22px;
    font-size: 27px;
    color: var(--title-light);
    background: linear-gradient(180deg, var(--title-light), var(--title-warm));
    -webkit-background-clip: text;
    background-clip: text;
    -webkit-text-fill-color: transparent;
    filter: drop-shadow(1px 2px 1px rgba(0,0,0,0.5));
    text-shadow: none;
  }
  .type-line {
    top: 198px;
    font-size: 28px;
    color: var(--title-light);
  }
  .scroll {
    position: absolute;
    left: 12px;
    width: 329px;
    box-sizing: border-box;
    padding: 8px 8px 9px;
    background: var(--scroll-edge);
    border-radius: 6px 6px 10px 10px / 6px 6px 6px 6px;
    box-shadow: inset 0 -4px 0 var(--scroll-shade), 0 2px 3px rgba(0,0,0,0.3);
  }
  .scroll-main { top: 60px; height: 132px; }
  .scroll-secondary { top: 234px; height: 238px; }
  .scroll-sheet {
    position: relative;
    height: 100%;
    background: var(--parchment);
    border-radius: 8px;
    display: flex;
    align-items: center;
    justify-content: center;
  }
  .rules-text {
    margin: 0;
    font-family: "Quicksand", sans-serif;
    font-weight: 600;
    font-size: 13px;
    line-height: 16.8px;
    color: var(--ink);
    text-align: center;
    letter-spacing: -0.2px;
  }
  .scroll-ornament {
    position: absolute;
    width: 40px;
    height: 60px;
    border-radius: 50%;
    background: rgba(214,190,180,0.35);
  }
  .ornament-top { left: 12px; top: 8px; }
  .ornament-bottom { right: 10px; bottom: 8px; }
</style>
</head>
<body>
  <article class="card">
    <div class="card-pattern" role="img" aria-label="Red Maori-inspired tribal carving pattern background"></div>

    <h1 class="card-title">Influenza Epidemic</h1>

    <section class="scroll scroll-main">
      <div class="scroll-sheet">
        <div class="scroll-ornament ornament-top" role="img" aria-label="Faint koru scroll ornament"></div>
        <div class="scroll-ornament ornament-bottom" role="img" aria-label="Faint koru scroll ornament"></div>
        <p class="rules-text">Lorem ipsum dolor sit amet, consectetur<br>adipiscing elit. In tempor purus nunc,<br>eu commodo tellus tempor at.<br>Etiam sit amet felis facilisis, convallis felis<br>tristique, cursus augue. Aenean eu ligula<br>quis nunc vulputate ultricies quis at ante.</p>
      </div>
    </section>

    <h2 class="type-line">Tribial</h2>

    <section class="scroll scroll-secondary">
      <div class="scroll-sheet">
        <div class="scroll-ornament ornament-top" role="img" aria-label="Faint koru scroll ornament"></div>
        <div class="scroll-ornament ornament-bottom" role="img" aria-label="Faint koru scroll ornament"></div>
        <p class="rules-text">Lorem ipsum dolor sit amet, consectetur<br>adipiscing elit. In tempor purus nunc,<br>eu commodo tellus tempor at.<br>Etiam sit amet felis facilisis, convallis felis<br>tristique, cursus augue.<br>Aenean eu ligula quis nunc vulputate ultricies<br>quis at ante. Etiam venenatis, lacus id ultrices<br>consequat, nibh elit fermentum leo, a interdum<br>nunc ipsum id ex.<br>Aliquam quis semper dolor.</p>
      </div>
    </section>
  </article>
</body>
</html>
```